Logo and label design for our product coffee scrub

We need a logo design and a packaging label design for our new brand called "Rocco Velvetine". Best design wins 500$

It's a cosmetic brand with initial product "coffee scrub", which is a body peeling made of coffee, himalayan salt and additives. Brand will target young to middle aged women, who we will address with a very sexy and slightly provocative appeal (pictures of women wearing nothing but our coffee scrub - sample attached). Purpose of the coffee scrub is to target cellulite, stretch marks, psoriasis, varicose veins, eczema and acne.

Packaging that we will use will be a brown stand up pouch (attached) with a dimensions width 13cm, height 22cm and with a front and back sticker (dimensions width 7cm, height 14cm, round corners) or sticker that overlaps from front to back.

Looking forward on receiving your ideas!

Target Market(s)

Brand will targeting young to middle aged european women, who we will address with a very sexy and slightly provocative appeal (pictures of women wearing nothing but our coffee scrub - sample attached)

Industry/Entity Type

Product

Requirements
Must have
• Just an idea for the logo writing to use a handwriting font "Rocco Velvetine".

For the front side of packaging label you could use a picture of a women's body wearing a coffee scrub. Label should be very sexy but not vulgar.
Nice to have
• The back side of the label should have a cheesy pick up line and declaration text (just a sample):

hi babe! so you wanna get dirty! just show me the way to your bath. but first let me give you a proper introduction of myself. my name is rocco and i'm a coffee scrub wearing nothing but 250g of finest arabic coffee and sweet orange flavour & lots of other good stuff.

by the way I will help you with cellulite, stretch marks, psoriasis, varicose veins, eczema and acne. i’ll smooth your lumps and bumps with brown sugar & sea salt, moisturise and tone your skin with cold pressed sweet almond oil, and use vitamins & minerals to work wonders from the outside in. then i’ll make us both smell good with a little orange essence.

ingredients:
Coffea Robusta Seed Powder (Coffee), Prunus Amygdalus Dulcis (Sweet Almond) Oil, Water (Aqua), Sodium Chloride (Salt), Sucrose (Brown Sugar). All ingredients organic.

net weight: 200 g

best before date:

barcode

```html
<!DOCTYPE html>
<html lang="en">
<head>
<meta charset="utf-8">
<title>Rocco Velvetine – Coffee Scrub Labels</title>
<link rel="stylesheet" href="https://fonts.googleapis.com/css2?family=Great+Vibes&display=swap">
<style>
  :root {
    --page: #ffffff;
    --kraft-light: #c9a77f;
    --kraft-mid: #b8936a;
    --kraft-dark: #a07a55;
    --floral-warm: #c0623f;
    --night: #000000;
    --floral-grey: #2e2e2e;
    --coral: #f0645f;
    --cream: #faf6cf;
    --white: #ffffff;
    --photo-light: #d9d4cf;
    --photo-dark: #5a4336;
  }
  * { box-sizing: border-box; margin: 0; padding: 0; }
  html, body {
    width: 1200px;
    height: 856px;
    overflow: hidden;
    background: var(--page);
  }
  .canvas {
    position: relative;
    width: 1200px;
    height: 856px;
  }
  .label {
    position: absolute;
    top: 12px;
    width: 546px;
    height: 826px;
    overflow: hidden;
  }
  .label--kraft { left: 20px; }
  .label--night { left: 642px; }

  .floral-pattern {
    position: absolute;
    inset: 0;
  }
  .label--kraft .floral-pattern {
    background:
      radial-gradient(ellipse 70% 18% at 50% 4%, rgba(192, 98, 63, 0.35), transparent 70%),
      radial-gradient(ellipse 70% 18% at 50% 97%, rgba(192, 98, 63, 0.35), transparent 70%),
      linear-gradient(160deg, var(--kraft-light), var(--kraft-mid) 55%, var(--kraft-dark));
  }
  .label--night .floral-pattern {
    background:
      radial-gradient(ellipse 70% 20% at 50% 5%, rgba(90, 90, 90, 0.45), transparent 70%),
      radial-gradient(ellipse 70% 20% at 50% 96%, rgba(90, 90, 90, 0.45), transparent 70%),
      radial-gradient(ellipse 80% 50% at 50% 50%, var(--floral-grey), var(--night) 80%);
  }

  .badge {
    position: absolute;
    left: 75px;
    top: 100px;
    width: 400px;
    height: 444px;
  }
  .badge__frame {
    fill: var(--coral);
    stroke: var(--cream);
    stroke-width: 10;
    stroke-linejoin: round;
  }

  .brand-name {
    position: absolute;
    left: 75px;
    top: 225px;
    width: 400px;
    text-align: center;
    font-family: "Great Vibes", cursive;
    font-weight: 400;
    font-size: 86px;
    line-height: 0.95;
    color: var(--white);
  }
  .brand-name span { display: block; }

  .model-photo {
    position: absolute;
    left: 200px;
    top: 494px;
    width: 132px;
    height: 132px;
    border-radius: 50%;
    border: 7px solid var(--cream);
    background: linear-gradient(135deg, var(--photo-light) 0%, var(--photo-light) 35%, var(--photo-dark) 100%);
  }

  .product-name {
    position: absolute;
    left: 0;
    top: 640px;
    width: 546px;
    text-align: center;
    font-family: "Great Vibes", cursive;
    font-size: 64px;
    line-height: 1;
    color: var(--white);
  }
  .label--kraft .product-name { left: -8px; }
</style>
</head>
<body>
<main class="canvas">

  <section class="label label--kraft">
    <div class="floral-pattern" role="img" aria-label="Warm hand-drawn floral pattern in rust, orange and brown on kraft paper"></div>
    <svg class="badge" viewBox="0 0 400 444" aria-hidden="true">
      <path class="badge__frame" d="M200 6 C225 32 260 44 315 42 C318 64 336 80 360 82 C358 112 372 128 394 132 C370 172 372 202 396 234 C372 264 368 302 362 352 C335 354 318 370 315 397 C265 397 230 412 200 438 C170 412 135 397 85 397 C82 370 65 354 38 352 C32 302 28 264 4 234 C28 202 30 172 6 132 C28 128 42 112 40 82 C64 80 82 64 85 42 C140 44 175 32 200 6 Z"/>
    </svg>
    <h1 class="brand-name"><span>Rocco</span><span>Velvetine</span></h1>
    <div class="model-photo" role="img" aria-label="Portrait photo of a woman wearing coffee scrub"></div>
    <p class="product-name">Coffee Scrub</p>
  </section>

  <section class="label label--night">
    <div class="floral-pattern" role="img" aria-label="Grey hand-drawn floral pattern on black"></div>
    <svg class="badge" viewBox="0 0 400 444" aria-hidden="true">
      <path class="badge__frame" d="M200 6 C225 32 260 44 315 42 C318 64 336 80 360 82 C358 112 372 128 394 132 C370 172 372 202 396 234 C372 264 368 302 362 352 C335 354 318 370 315 397 C265 397 230 412 200 438 C170 412 135 397 85 397 C82 370 65 354 38 352 C32 302 28 264 4 234 C28 202 30 172 6 132 C28 128 42 112 40 82 C64 80 82 64 85 42 C140 44 175 32 200 6 Z"/>
    </svg>
    <h2 class="brand-name"><span>Rocco</span><span>Velvetine</span></h2>
    <div class="model-photo" role="img" aria-label="Portrait photo of a woman wearing coffee scrub"></div>
    <p class="product-name">Coffee Scrub</p>
  </section>

</main>
</body>
</html>
```